Need business cards for our e-assessment business

We need professional looking business cards for our e-assessment business based in Europe. Our company is called Velnor.

You can just use sample name and addresses.

The colours we use are:

#70abe4 (blue)
#FF6600 (orange)

The back side should say: E-assessment made easy

This is the print-shop we are using. Please look at the link for info about formats: http://nl.printqet.com/help/faq/using-my-own-artwork.html

Target Market(s)

Target market is education and large corporations

Industry/Entity Type

Business

```html
<!DOCTYPE html>
<html lang="en">
<head>
<meta charset="utf-8">
<title>Velnor business cards</title>
<link rel="stylesheet" href="https://fonts.googleapis.com/css2?family=Mulish:wght@300;400;700&display=swap">
<style>
  :root {
    --blue: #70abe4;
    --orange: #ef7a1f;
    --ink: #444444;
    --ink-soft: #333333;
    --white: #ffffff;
    --page: #ffffff;
  }
  * { margin: 0; padding: 0; box-sizing: border-box; }
  html, body {
    width: 991px;
    height: 1200px;
    overflow: hidden;
    background: var(--page);
    font-family: "Mulish", "Century Gothic", sans-serif;
  }
  .sheet { position: relative; width: 991px; height: 1200px; }

  .card {
    position: absolute;
    filter: drop-shadow(0 2px 6px rgba(0,0,0,0.18));
  }
  .card svg.card-shape { position: absolute; inset: 0; display: block; }

  /* Front */
  .card-front { left: 131px; top: 98px; width: 657px; height: 437px; }
  .brand-mark {
    position: absolute; left: 63px; top: 61px;
    width: 134px; height: 134px; border-radius: 50%;
    background: var(--orange);
  }
  .brand-name {
    position: absolute; left: 235px; top: 66px;
    font-size: 100px; font-weight: 400; line-height: 1;
    color: var(--ink); letter-spacing: -1px;
  }
  .person {
    position: absolute; right: 455px; top: 274px; text-align: right;
    color: var(--ink-soft);
  }
  .person-name { font-size: 21px; font-weight: 700; line-height: 26px; }
  .person-role { font-size: 19px; font-weight: 400; line-height: 26px; }
  .contacts {
    position: absolute; left: 256px; top: 244px; list-style: none;
  }
  .contacts li {
    display: flex; align-items: center; height: 31px;
    font-size: 19px; color: var(--ink-soft);
  }
  .contacts svg { width: 18px; height: 18px; margin-right: 29px; flex: none; }

  /* Back */
  .card-back { left: 138px; top: 620px; width: 656px; height: 438px; }
  .back-mark {
    position: absolute; left: 242px; top: 92px;
    width: 152px; height: 152px; border-radius: 50%;
    background: var(--white);
  }
  .tagline {
    position: absolute; left: 0; right: 0; top: 282px;
    text-align: center; color: var(--white);
    font-size: 47px; font-weight: 300; letter-spacing: 0.5px;
  }
</style>
</head>
<body>
<main class="sheet">

  <section class="card card-front" aria-label="Business card front">
    <svg class="card-shape" width="657" height="437" viewBox="0 0 657 437">
      <defs>
        <linearGradient id="front-fade" x1="0" x2="1" y1="0" y2="0">
          <stop offset="0" stop-color="var(--blue)"/>
          <stop offset="0.2" stop-color="#ffffff"/>
          <stop offset="0.73" stop-color="#ffffff"/>
          <stop offset="1" stop-color="var(--blue)"/>
        </linearGradient>
      </defs>
      <path d="M0,437 L0,160 C0,40 45,0 165,0 L657,0 L657,250 C657,385 615,437 480,437 Z" fill="url(#front-fade)"/>
    </svg>
    <div class="brand-mark"></div>
    <div class="brand-name">velnor</div>
    <div class="person">
      <p class="person-name">Your Name</p>
      <p class="person-role">Position</p>
    </div>
    <ul class="contacts">
      <li>
        <svg viewBox="0 0 24 24" fill="var(--orange)"><path d="M6.6 2.5l3 3.2-1.8 2.6c1.2 2.7 3.2 4.8 5.9 6l2.6-1.8 3.2 3-1.7 3.5C10 18.6 5.4 14 3.1 6.2z"/></svg>
        123-456-7890
      </li>
      <li>
        <svg viewBox="0 0 24 24" fill="none" stroke="var(--orange)" stroke-width="2"><rect x="6" y="2" width="12" height="20" rx="2"/><line x1="6" y1="17" x2="18" y2="17"/></svg>
        123-456-7888
      </li>
      <li>
        <svg viewBox="0 0 24 24" fill="none" stroke="var(--orange)" stroke-width="2"><rect x="2" y="5" width="20" height="14"/><path d="M2 5l10 8 10-8M2 19l7-7M22 19l-7-7"/></svg>
        name@velnor.com.eu
      </li>
      <li>
        <svg viewBox="0 0 24 24" fill="none" stroke="var(--orange)" stroke-width="2"><circle cx="12" cy="12" r="10"/><ellipse cx="12" cy="12" rx="4" ry="10"/><line x1="12" y1="2" x2="12" y2="22"/></svg>
        www.velnor.com.eu
      </li>
    </ul>
  </section>

  <section class="card card-back" aria-label="Business card back">
    <svg class="card-shape" width="656" height="438" viewBox="0 0 656 438">
      <path d="M0,0 L500,0 C620,0 656,60 656,190 L656,438 L150,438 C40,438 0,395 0,280 Z" fill="var(--orange)"/>
    </svg>
    <div class="back-mark"></div>
    <p class="tagline">E-assessment made easy</p>
  </section>

</main>
</body>
</html>
```